Blue Heron Journeys

We are a predominantly online travel agency with high-end (first/business class) clients. I'm looking to either have our existing logo revamped or a new logo created with business card layout. I prefer to work with existing logo if possible so it remains familiar with existing clientele. I have uploaded a yellow business card layout showing icons on one side of the card. I would like to keep my existing colours, not yellow. could the company name/tag line go over the icons?
Contact Information for Business Card
Colleen Fairbank
Director
(G.T.L.C. 07815364)
(Quorvanel Pty. Ltd) ABN 61 507 314 829
512/48 Tillbrook Street
Calder Heights | NSW 2468 | Australia
www.blueheronjourneys-example.com.au
m: + 61 (0) 491 738 052
t: + 61 (0) 2 9175 3816
e: colleen@blueheronjourneys-example.com.au

```html
<!DOCTYPE html>
<html lang="en">
<head>
<meta charset="utf-8">
<title>Blue Heron Journeys – Business Cards</title>
<link rel="stylesheet" href="https://fonts.googleapis.com/css2?family=Source+Sans+3:wght@400;600&display=swap">
<style>
  :root {
    --backdrop: #272727;
    --kraft-light: #dcbf96;
    --kraft-mid: #c6a273;
    --kraft-dark: #a77f4f;
    --ink: #1c1712;
    --ink-soft: #2a221a;
    --rule: #5a4836;
  }
  * { margin: 0; padding: 0; box-sizing: border-box; }
  html, body { width: 1200px; height: 900px; overflow: hidden; }
  body {
    background: var(--backdrop);
    position: relative;
    font-family: "Source Sans 3", "Myriad Pro", sans-serif;
    color: var(--ink);
  }
  .card {
    position: absolute;
    top: 307px;
    width: 439px;
    height: 270px;
    background: radial-gradient(ellipse at 45% 0%, var(--kraft-light) 0%, var(--kraft-mid) 55%, var(--kraft-dark) 100%);
  }
  .card--front { left: 150px; }
  .card--back { left: 609px; }

  .brand-name {
    position: absolute;
    left: 0; right: 0;
    text-align: center;
    font-family: "Source Sans 3", sans-serif;
    font-weight: 400;
    color: var(--ink);
    white-space: nowrap;
  }
  .card--front .brand-name { top: 56px; font-size: 36px; }
  .card--back .brand-name { top: 100px; font-size: 43px; }

  .holder {
    position: absolute;
    left: 30px;
    top: 161px;
    font-size: 13px;
    line-height: 16px;
    color: var(--ink-soft);
  }
  .holder-name {
    font-size: 16px;
    font-weight: 600;
    line-height: 20px;
    color: var(--ink);
    letter-spacing: 0.2px;
  }
  .holder-rule {
    position: absolute;
    left: 145px;
    top: 170px;
    width: 266px;
    height: 1px;
    background: var(--rule);
  }
  .contact-list {
    position: absolute;
    right: 24px;
    top: 193px;
    list-style: none;
    font-size: 13px;
    line-height: 16px;
    color: var(--ink-soft);
    text-align: right;
  }
  .contact-list li { display: flex; align-items: center; justify-content: flex-end; gap: 4px; }
  .contact-icon { width: 9px; height: 9px; flex: none; }
</style>
</head>
<body>
  <section class="card card--front" aria-label="Business card front">
    <div class="brand-name">Blue Heron Journeys</div>

    <div class="holder-rule"></div>
    <div class="holder">
      <div class="holder-name">LORUM SMITH</div>
      <div>Managing Director</div>
      <div>421, Address line here,</div>
      <div>Dummy Code,</div>
      <div>45452Country Name</div>
    </div>

    <ul class="contact-list">
      <li>888 444 0000
        <svg class="contact-icon" viewBox="0 0 9 9" aria-hidden="true"><rect x="2.5" y="0.5" width="4" height="8" rx="0.8" fill="none" stroke="#2a221a" stroke-width="1"/></svg>
      </li>
      <li>info@webname.com
        <svg class="contact-icon" viewBox="0 0 9 9" aria-hidden="true"><rect x="0.5" y="1.5" width="8" height="6" fill="#2a221a"/><path d="M0.5 1.8 L4.5 5 L8.5 1.8" fill="none" stroke="#c6a273" stroke-width="0.8"/></svg>
      </li>
      <li>www.webaddress.com
        <svg class="contact-icon" viewBox="0 0 9 9" aria-hidden="true"><circle cx="4.5" cy="4.5" r="4" fill="#2a221a"/><path d="M0.5 4.5 H8.5 M4.5 0.5 C2.5 3 2.5 6 4.5 8.5 M4.5 0.5 C6.5 3 6.5 6 4.5 8.5" fill="none" stroke="#c6a273" stroke-width="0.6"/></svg>
      </li>
    </ul>
  </section>

  <section class="card card--back" aria-label="Business card back">
    <div class="brand-name">Blue Heron Journeys</div>
  </section>
</body>
</html>
```